People Analytics Company needs Web Design and CSS

We need a refreshed design for a People Analytics company called VOMTA Systems Inc. We have developed an online survey tool that our immediate need is to make it look snazzier for upcoming pilots with prospective companies. Dark Blue and Orange are the colors we like to use but the survey should be "neutral" - we don't want to influence any responses based on colors.

Target Market(s)

Enterprise Users

Industry/Entity Type

It Company

Coding

Coded - Design and coding required

Number of Pages Required

3 page

Font styles to use
Sans Serif

Colors
0556a4
f37122

Requirements
Must have
• User friendly way of responding to survey questions that is suitable for a tablet (fat fingers). Drag and Drop is also very hard on tablet.
• Neutral look and feel to reduce any potential respondent bias.
• Colors consistent with brand colors attached in document.
• Minimal scrolling is best.
Should not have
• Too many colors.

```html
<!DOCTYPE html>
<html lang="en">
<head>
<meta charset="utf-8">
<title>VOMTA Systems Inc. — Survey Demo</title>
<link href="https://fonts.googleapis.com/css2?family=Quicksand:wght@500;700&family=Cabin:wght@400;600&display=swap" rel="stylesheet">
<style>
  :root {
    --orange: #f37122;
    --blue: #0556a4;
    --navy: #0a1035;
    --cream: #f7f7f0;
    --grey: #aeaaa7;
    --row-light: #f4f4f4;
    --row-white: #fdfdfd;
    --row-blue: #e9f1fb;
    --rule: #e2e2e2;
    --ink: #2d2d2d;
    --ink-soft: #555;
    --white: #ffffff;
  }
  * { box-sizing: border-box; margin: 0; padding: 0; }
  html, body { width: 1200px; height: 960px; overflow: hidden; }
  body { position: relative; background: var(--white); font-family: "Cabin", sans-serif; color: var(--ink); }

  .site-header { position: absolute; left: 0; top: 0; width: 1200px; height: 97px; background: var(--cream); }
  .nav-btn {
    position: absolute; top: 0; width: 83px; height: 97px;
    display: flex; align-items: center; justify-content: center;
    font-family: "Quicksand", sans-serif; font-weight: 700; font-size: 11px;
    letter-spacing: 1.2px; color: var(--white); text-decoration: none;
  }
  .nav-home { left: 171px; background: var(--orange); }
  .nav-logout { left: 945px; background: var(--blue); }
  .brand { position: absolute; left: 520px; top: 20px; width: 160px; height: 58px; display: flex; align-items: center; gap: 8px; }
  .brand-mark { width: 14px; height: 14px; background: var(--orange); border-radius: 50%; flex: none; }
  .brand-name { font-family: "Quicksand", sans-serif; font-weight: 700; font-size: 15px; color: var(--navy); line-height: 1.15; }

  .survey { position: absolute; left: 171px; top: 152px; width: 857px; }
  .survey-intro {
    height: 73px; background: var(--grey); border-radius: 5px 5px 0 0;
    border-bottom: 3px solid var(--white); box-shadow: 0 2px 0 var(--grey);
    display: flex; align-items: center; justify-content: center; text-align: center;
    font-family: "Quicksand", sans-serif; font-weight: 500; font-size: 12px;
    letter-spacing: 1px; line-height: 19px; color: var(--white); padding: 0 60px;
  }
  .survey-intro strong { font-weight: 700; }

  .scale-table { width: 857px; margin-top: 4px; border-collapse: collapse; table-layout: fixed; }
  .scale-table th {
    height: 53px; background: var(--row-light); border: 1px solid var(--rule);
    font-family: "Quicksand", sans-serif; font-weight: 500; font-size: 9.5px;
    letter-spacing: 1px; line-height: 12px; color: #444;
  }
  .scale-table td { border: 1px solid var(--rule); vertical-align: top; }
  .scale-table col.statement { width: 183px; }
  .scale-table col.choice { width: 123px; }
  .row-blue td { background: var(--row-blue); }
  .row-white td { background: var(--row-white); }
  .row-light td { background: var(--row-light); }
  .scale-table td.chosen { background: var(--grey); vertical-align: middle; text-align: center; }
  .tick { width: 18px; height: 18px; display: inline-block; }

  .statement-cell { padding: 14px 10px 0 12px; }
  .statement-topic {
    font-family: "Quicksand", sans-serif; font-weight: 700; font-size: 10.5px;
    letter-spacing: 0.8px; color: #111; display: flex; align-items: center; margin-bottom: 8px;
  }
  .statement-topic::before { content: ""; width: 5px; height: 5px; border-radius: 50%; background: #111; margin-right: 10px; }
  .statement-text { font-size: 9.5px; line-height: 13.4px; color: var(--ink-soft); }
  .statement-text b { font-weight: 600; color: #333; }

  .submit-btn {
    position: absolute; left: 543px; top: 769px; width: 112px; height: 43px;
    background: var(--grey); color: var(--white); display: flex; align-items: center; justify-content: center; gap: 8px;
    font-family: "Quicksand", sans-serif; font-weight: 700; font-size: 12px; letter-spacing: 2px; border: none;
  }

  .site-footer { position: absolute; left: 0; top: 865px; width: 1200px; height: 95px; background: var(--navy); }
  .copyright {
    position: absolute; left: 173px; top: 40px; font-family: "Quicksand", sans-serif; font-weight: 700;
    font-size: 9.5px; letter-spacing: 0.8px; color: var(--white);
  }
  .copyright a { color: var(--orange); text-decoration: none; }
  .footer-brand { position: absolute; left: 572px; top: 37px; display: flex; align-items: center; gap: 6px;
    font-family: "Quicksand", sans-serif; font-weight: 700; font-size: 13px; color: var(--white); }
  .footer-brand span.mark { width: 10px; height: 10px; background: var(--orange); }
  .social { position: absolute; left: 923px; top: 42px; display: flex; gap: 22px; }
  .social span { width: 10px; height: 10px; border-radius: 50%; background: #9fa3b8; }
</style>
</head>
<body>
  <header class="site-header">
    <a class="nav-btn nav-home" href="#">HOME</a>
    <div class="brand"><span class="brand-mark"></span><span class="brand-name">VOMTA<br>Systems Inc.</span></div>
    <a class="nav-btn nav-logout" href="#">LOGOUT</a>
  </header>

  <main class="survey">
    <p class="survey-intro"><span><strong>This is a demo of the types of questions we have in our survey.</strong> This set of questions are the five that are best predictors of how well someone might feel they fit in <strong>their role as an Executive.</strong></span></p>

    <table class="scale-table">
      <colgroup>
        <col class="statement"><col class="choice"><col class="choice"><col class="choice"><col class="choice"><col class="statement">
      </colgroup>
      <thead>
        <tr>
          <th>Statements</th>
          <th>Left Statement<br>Much Better</th>
          <th>Left Statement<br>Better</th>
          <th>Right Statement<br>Better</th>
          <th>Right Statement<br>Much Better</th>
          <th>Statements</th>
        </tr>
      </thead>
      <tbody>
        <tr class="row-blue" style="height:99px">
          <td class="statement-cell"><p class="statement-topic">Colleagues :</p><p class="statement-text"><b>Work-life-balancer</b> - Someone who is unlikely to bother you during an evening or weekend, but is also unlikely to help you after hours.</p></td>
          <td class="chosen"><svg class="tick" viewBox="0 0 18 18"><path d="M2 10 L7 15 L16 3" fill="none" stroke="#fff" stroke-width="1.8"/></svg></td>
          <td></td><td></td><td></td>
          <td class="statement-cell"><p class="statement-topic">Colleagues :</p><p class="statement-text"><b>Always on -</b> Available to answer questions at anytime, but may ask questions at any time and expect answers.</p></td>
        </tr>
        <tr class="row-white" style="height:114px">
          <td class="statement-cell"><p class="statement-topic">Cultures :</p><p class="statement-text"><b>Right the first time -</b> Follow the tried and tested ways that help the job get done right the first time, may need to rework in the future as things change.</p></td>
          <td></td>
          <td class="chosen"><svg class="tick" viewBox="0 0 18 18"><path d="M2 10 L7 15 L16 3" fill="none" stroke="#fff" stroke-width="1.8"/></svg></td>
          <td></td><td></td>
          <td class="statement-cell"><p class="statement-topic">Cultures :</p><p class="statement-text"><b>Failed Experiments -</b> Experiment, iterate and find ways that might fail early, success in the future will be more sustainable.</p></td>
        </tr>
        <tr class="row-light" style="height:80px">
          <td class="statement-cell"><p class="statement-topic">Attitudes :</p><p class="statement-text">A Team will get likely get stuck without a leader.</p></td>
          <td></td><td></td>
          <td class="chosen"><svg class="tick" viewBox="0 0 18 18"><path d="M2 10 L7 15 L16 3" fill="none" stroke="#fff" stroke-width="1.8"/></svg></td>
          <td></td>
          <td class="statement-cell"><p class="statement-topic">Attitudes :</p><p class="statement-text">A Team will figure out what needs to be done, even without a leader.</p></td>
        </tr>
        <tr class="row-white" style="height:85px">
          <td class="statement-cell"><p class="statement-topic">Attitudes :</p><p class="statement-text">It is better for a leader to listen to what other have to say first before sharing an opinion in discussion.</p></td>
          <td></td><td></td><td></td>
          <td class="chosen"><svg class="tick" viewBox="0 0 18 18"><path d="M2 10 L7 15 L16 3" fill="none" stroke="#fff" stroke-width="1.8"/></svg></td>
          <td class="statement-cell"><p class="statement-topic">Attitudes :</p><p class="statement-text">It is better for a leader to share an opinion first to start a discussion.</p></td>
        </tr>
        <tr class="row-light" style="height:74px">
          <td class="statement-cell"><p class="statement-topic">Attitudes :</p><p class="statement-text">It is better for teams to have many, but small wins.</p></td>
          <td></td><td></td>
          <td class="chosen"><svg class="tick" viewBox="0 0 18 18"><path d="M2 10 L7 15 L16 3" fill="none" stroke="#fff" stroke-width="1.8"/></svg></td>
          <td></td>
          <td class="statement-cell"><p class="statement-topic">Attitudes :</p><p class="statement-text">It is better for teams to have fewer, but bigger wins.</p></td>
        </tr>
      </tbody>
    </table>
  </main>

  <button class="submit-btn" type="button">SUBMIT
    <svg width="11" height="9" viewBox="0 0 11 9"><path d="M0 4.5 H7 M5 1 L9.5 4.5 L5 8" fill="none" stroke="#fff" stroke-width="1.8"/></svg>
  </button>

  <footer class="site-footer">
    <p class="copyright">Copyrights © 2015. All Rights Reserved. <a href="#">VOMTA.io</a></p>
    <div class="footer-brand"><span class="mark"></span>VOMTA</div>
    <div class="social" aria-label="Social links"><span></span><span></span><span></span><span></span></div>
  </footer>
</body>
</html>
```